Packaging / Logo Design for Toddler Potty Liners

We need a packaging and logo design for a new company based in Atlanta called "WeeMeadow". We manufacture innovative, eco-friendly baby / toddler products. Our initial product is a flushable, biodegradable potty liner used for toddler potty training. We are looking for a modern / clean / eco-friendly packaging and logo design for this product. Each package will contain 20 liners. Box dimensions are as follows:

Length = 8.5in
Width = 5in
Height = 1.5in

The box will have a perforated top measuring 6.5 inches (see attached pictures). Liners will be folded inside and individually pulled out through the perforated top (similar to a Softrel box). See attached pictures of similar box.

Packaging should appeal to parents as an easy to use, eco-friendly, sanitary solution to potty training. This product is an alternative to the conventional way of cleaning / disinfecting the potty after each use, a process that most parents dread!

The closest competitors are NeatNips (www.neatnips-example.com) and Brillo (www.brillo-example.com) - you can reference their websites to get an idea for the product and use. However, their liners are not flushable and that is the biggest differentiator of this product. Their packaging seems conventional and non-inspiring so we would like our design to stand out from theirs.

We would like to see creative, modern cardboard box designs which will make our brand stand out from the competition. We would like to use one of the following color schemes: 1) a modern green color on a white background, 2) a modern green color on plain cardboard background, or 3) white on a modern green background. May use one or two additional complementary colors. See attached modern green image for inspiration. We would like to see clean lines, text and illustrations. We are looking forward to seeing any cool ideas you may have!
Updates

Brief has been updated with our desired color schemes and pictures for inspiration.  Please read updated brief before beginning your design!  Thanks so much!

Industry/Entity Type

Biodegradable

Requirements
Must have
• The front of the package should include the following info:

Logo: WeeMeadow
Product Name: Flushable Potty Chair Liners
Clean and Convenient
Fits All Potty Chairs
Sewer and Septic Safe
Patent Pending
20 Single-Use Flushable Potty Chair Liners

Package should also have space for some simple instructions (preferably with illustrations). This can be placed on one of the sides of the box.
1. Place liner over clean, dry (underline the word dry) potty bowl.
2. After your toddler uses the potty, remove liner (do not tie) and flush.
3. Give your toddler a high five!

Please submit design considering all sides of the box!

```html
<!DOCTYPE html>
<html lang="en">
<head>
<meta charset="utf-8">
<title>WeeMeadow Flushable Potty Chair Liners – Box Panels</title>
<link rel="stylesheet" href="https://fonts.googleapis.com/css2?family=Bree+Serif&family=Oswald:wght@400;500&family=Open+Sans:wght@400;600&family=Lobster+Two:ital@1&display=swap">
<style>
  :root {
    --kraft: #b2a68f;
    --kraft-dark: #a3967e;
    --green: #1f8a22;
    --pattern-green: #5f9a48;
    --pattern-kraft: #8fa06a;
    --blue: #4a6ea3;
    --cream: #efe6cf;
    --page: #ffffff;
  }
  * { margin: 0; padding: 0; box-sizing: border-box; }
  html, body {
    width: 1200px; height: 848px; overflow: hidden;
    background: var(--page);
  }
  .canvas { position: relative; width: 1200px; height: 848px; }

  /* Top panel */
  .top-panel {
    position: absolute; left: 150px; top: 72px;
    width: 900px; height: 529px;
    background: radial-gradient(circle at 30% 40%, var(--kraft) 0%, var(--kraft-dark) 100%);
    text-align: center;
    color: var(--green);
  }
  .brand {
    position: absolute; left: 0; right: 0; top: 40px;
    display: flex; flex-direction: column; align-items: center;
  }
  .brand-dot {
    width: 76px; height: 76px; border-radius: 50%;
    background: var(--green);
  }
  .brand-name {
    margin-top: 10px;
    font-family: "Bree Serif", serif; font-weight: 400;
    font-size: 58px; line-height: 1;
    color: var(--blue);
    letter-spacing: -0.5px;
  }

  .claims {
    position: absolute; left: 50%; top: 318px;
    width: 316px; transform: translateX(-50%);
    display: flex; flex-direction: column; align-items: stretch;
  }
  .tagline {
    display: flex; align-items: center; gap: 8px;
    font-family: "Lobster Two", cursive; font-style: italic;
    font-size: 22px; color: var(--green); line-height: 1;
  }
  .tagline::before, .tagline::after {
    content: ""; flex: 1; height: 8px; background: var(--green);
  }
  .product-name {
    margin-top: 6px;
    font-family: "Oswald", sans-serif; font-weight: 500;
    font-size: 21px; letter-spacing: 0.5px; color: var(--green);
    border-bottom: 3px solid var(--green); padding-bottom: 2px;
  }
  .fit-band {
    margin-top: 8px;
    background: var(--blue); color: var(--cream);
    font-family: "Bree Serif", serif; font-size: 24px;
    padding: 3px 0 5px;
    border-top: 2px dotted var(--cream);
    border-bottom: 2px dotted var(--cream);
  }
  .safe-line {
    margin-top: 8px;
    font-family: "Oswald", sans-serif; font-size: 18px;
    color: var(--green); letter-spacing: 0.3px;
    border-top: 2px solid var(--green); border-bottom: 2px solid var(--green);
    padding: 1px 0;
  }
  .patent {
    margin-top: 4px;
    font-family: "Open Sans", sans-serif; font-size: 16px; color: var(--green);
  }
  .count {
    font-family: "Open Sans", sans-serif; font-size: 11px; color: var(--green);
  }

  /* Side panel with instructions */
  .side-panel {
    position: absolute; left: 150px; top: 618px;
    width: 900px; height: 158px;
    background: var(--kraft);
    font-family: "Open Sans", sans-serif; color: var(--green);
    overflow: hidden;
  }
  .pattern-frame {
    position: absolute; inset: 0;
    background: linear-gradient(90deg, var(--pattern-green), var(--pattern-kraft) 50%, var(--pattern-green));
  }
  .steps {
    position: absolute; left: 44px; right: 44px; top: 22px; bottom: 22px;
    background: var(--kraft);
    display: grid; grid-template-columns: repeat(3, 1fr);
    align-items: center;
    padding: 0 18px;
  }
  .step {
    display: flex; align-items: center; gap: 14px;
  }
  .step-art {
    width: 84px; height: 84px; flex: none;
    background: var(--green); border-radius: 10px;
  }
  .step-text { font-size: 13px; line-height: 1.35; width: 150px; }
  .step-text u { text-decoration-thickness: 1.5px; }
</style>
</head>
<body>
<main class="canvas">

  <section class="top-panel" aria-label="Box top">
    <div class="brand">
      <span class="brand-dot"></span>
      <h1 class="brand-name">WeeMeadow</h1>
    </div>

    <div class="claims">
      <p class="tagline">clean and convenient</p>
      <h2 class="product-name">FLUSHABLE POTTY CHAIR LINERS</h2>
      <p class="fit-band">fits all potty chairs</p>
      <p class="safe-line">SEWER AND SEPTIC SAFE</p>
      <p class="patent">patent pending</p>
      <p class="count">20 single-use flushable potty chair liners</p>
    </div>
  </section>

  <section class="side-panel" aria-label="Box side with instructions">
    <div class="pattern-frame" role="img" aria-label="Green polka dot pattern around the side panel"></div>

    <div class="steps">
      <div class="step">
        <div class="step-art" role="img" aria-label="Illustration of a liner placed over a potty bowl"></div>
        <p class="step-text">place liner over clean, <u>dry</u> potty bowl!</p>
      </div>
      <div class="step">
        <div class="step-art" role="img" aria-label="Illustration of a liner being dropped into a toilet"></div>
        <p class="step-text">after your toddler uses the potty, remove liner (do not tie) and flush</p>
      </div>
      <div class="step">
        <div class="step-art" role="img" aria-label="Illustration of a raised hand for a high five"></div>
        <p class="step-text">give your toddler a high five!</p>
      </div>
    </div>
  </section>

</main>
</body>
</html>
```